Sangria Label

We are a small family winery in central Florida who is developing a sangria called Twirl, Clink & Hum Along Sangria !!

Who doesn't like sangria ?? It's a fun drink that you would serve at backyard BBQ's, Tiki Bars, casual party's, bridal showers, etc., and we have given our sangria a fun name !!

My partner wants me to request some designs with the following guidelines:

To illustrate Twirl, Clink & Hum Along, he would like to see a label depicting, from left to right, a drawing of a hopscotch board, then a lemonade stand with the word LEMONADE crossed out but readable and the word SANGRIA put in its place. On the Lemonade stand are cups that have fallen over with some lemonade flowing out. The final illustration on the right would be of someone running off the label with an article of clothing being tossed off that person.

Requirements
Must have
• Try to make the design colorful, fun, and playful
Nice to have
• We like the Black Cherry Moon Font but are open to other ideas

We think we would like to have the words Twirl, Clink & Hum Along in a curved fashion at the top of the label and the word Sangria !! at the bottom of the label........but we are open to other ideas.
Should not have
• no flower images

```html
<!DOCTYPE html>
<html lang="en">
<head>
<meta charset="utf-8">
<title>Twirl, Clink &amp; Hum Along Sangria Label</title>
<link href="https://fonts.googleapis.com/css2?family=Amatic+SC:wght@400;700&display=swap" rel="stylesheet">
<style>
  :root {
    --paper: #ffffff;
    --label-green: #7dff00;
    --border-yellow: #d6ee2a;
    --emblem-lime: #b9fb16;
    --tagline-blue: #5a9bf0;
    --title-pink: #e4005e;
  }
  html, body {
    margin: 0;
    padding: 0;
    width: 1197px;
    height: 1200px;
    overflow: hidden;
    background: var(--paper);
  }
  .label {
    display: block;
    width: 1197px;
    height: 1200px;
  }
  .label__field { fill: var(--label-green); }
  .label__border-band { fill: var(--border-yellow); opacity: 0.55; }
  .label__emblem { fill: var(--emblem-lime); }
  .label__tagline {
    font-family: "Amatic SC", "Comic Sans MS", cursive;
    font-weight: 400;
    font-size: 150px;
    fill: var(--tagline-blue);
  }
  .label__title {
    font-family: "Amatic SC", "Comic Sans MS", cursive;
    font-weight: 700;
    font-size: 340px;
    fill: var(--title-pink);
  }
</style>
</head>
<body>
<svg class="label" viewBox="0 0 1197 1200" xmlns="http://www.w3.org/2000/svg">
  <rect class="label__field" x="86" y="86" width="1028" height="1026"/>

  <path class="label__border-band" role="img" aria-label="Zigzag border of small yellow triangles around the label edge"
        fill-rule="evenodd"
        d="M86 86 H1114 V1112 H86 Z M127 127 V1071 H1073 V127 Z"/>

  <text class="label__tagline" x="185" y="330" textLength="825" lengthAdjust="spacingAndGlyphs"
        transform="rotate(3 597 300)">Twirl, Clink, &amp; Hum Along!</text>

  <polygon class="label__emblem" role="img" aria-label="Geometric octagonal sun emblem in lime tones"
           points="530,356 658,356 748,448 748,576 658,666 530,666 440,576 440,448"/>

  <text class="label__title" x="245" y="985" textLength="685" lengthAdjust="spacingAndGlyphs">Sangria</text>
</svg>
</body>
</html>
```